Soy Candle Business needs a label design

We need a label design for a new company selling soy candles - Velvet Hearth Studio.

We are using apothecary jars in 3 sizes.
As per attached candles will be dressed with a beautiful black bow and all finished with a diamante in centre of bow.

We would like label done on lid of candle jars - 5cm circle (5cm from one side to the other), this way one label will fit each product size. Label will be done as a sticker.

We are thinking of the background colour to be black, however are open to recommendations. We want label to be classy, elegant and simple.

Inspiration for candle design came from attached invitation that features the bow, and beautiful vintage paper on top area.

Label should include the following 3 pieces of information:
Velvet Hearth Studio (company name)
Coconut Lime (this will change depending on fragrance)
Soy Candle

Velvet Hearth Studio does not have a company logo... what is done for the label will set tone for what is done across other elements of business moving forward.

Industry/Entity Type

Business

Requirements
Must have
• Velvet Hearth Studio
Fragrance Flavour
Soy Candle

```html
<!DOCTYPE html>
<html lang="en">
<head>
<meta charset="utf-8">
<title>Velvet Hearth Studio – Lid Label</title>
<link rel="stylesheet" href="https://fonts.googleapis.com/css2?family=Pinyon+Script&family=Marcellus&display=swap">
<style>
  :root {
    --page-bg: #ecebea;
    --label-black: #0b0b0b;
    --label-deep: #1c1c1c;
    --ring-white: #f4f2ee;
    --text-white: #f7f5f0;
    --text-soft: #dcd9d2;
  }
  * { margin: 0; padding: 0; box-sizing: border-box; }
  html, body {
    width: 757px;
    height: 1200px;
    overflow: hidden;
    background: var(--page-bg);
  }
  .canvas {
    position: relative;
    width: 757px;
    height: 1200px;
  }
  .lid-label {
    position: absolute;
    left: 48px;
    top: 270px;
    width: 660px;
    height: 660px;
  }
  .lid-label__art {
    position: absolute;
    inset: 0;
    width: 100%;
    height: 100%;
  }
  .lid-label__text {
    position: absolute;
    inset: 0;
    text-align: center;
    color: var(--text-white);
  }
  .brand-name {
    position: absolute;
    left: 0;
    right: 0;
    top: 220px;
    font-family: "Pinyon Script", cursive;
    font-size: 66px;
    line-height: 1;
    font-weight: 400;
  }
  .fragrance,
  .product-type {
    position: absolute;
    left: 0;
    right: 0;
    font-family: "Marcellus", serif;
    font-size: 38px;
    line-height: 1;
    letter-spacing: 1px;
    color: var(--text-soft);
  }
  .fragrance { top: 366px; }
  .product-type { top: 412px; }
</style>
</head>
<body>
  <main class="canvas">
    <section class="lid-label">
      <svg class="lid-label__art" viewBox="0 0 660 660" xmlns="http://www.w3.org/2000/svg">
        <defs>
          <radialGradient id="label-fill" cx="50%" cy="45%" r="55%">
            <stop offset="0%" stop-color="var(--label-deep)"/>
            <stop offset="100%" stop-color="var(--label-black)"/>
          </radialGradient>
        </defs>
        <circle cx="330" cy="330" r="330" fill="var(--label-black)"/>
        <circle cx="330" cy="330" r="318" fill="none" stroke="var(--ring-white)" stroke-width="5"/>
        <circle cx="330" cy="330" r="312" fill="url(#label-fill)" role="img" aria-label="Faint dark grey vintage flourish pattern across the label background"/>
      </svg>
      <div class="lid-label__text">
        <h1 class="brand-name">Velvet Hearth Studio</h1>
        <p class="fragrance">Coconut Lime</p>
        <p class="product-type">Soy Candle</p>
      </div>
    </section>
  </main>
</body>
</html>
```